Expense Tracker App for Young Adults

I need a mobile app designer to design an app UI for me. It is for an expense tracker app. I’ve attached a mind map of the various screens and features of the app.

I would like to see designs for this app which is targeted towards young adults (late teens & early 20s) just starting their career who want to plan their budgets and track their expenses.
Updates

Hello designers! I'm conscious that this is not a guaranteed project, so I can understand that some of you might be apprehensive. Just wanted to let you know that I'm willing to see your initial drafts that show your direction and theme for design. You don't have to design the whole app. In fact, it's better if you share your initial design ideas so that we can have a discussion and I can give my input. If I see some good initial designs, I will be happy to make this a guaranteed project. I'm simply being cautious since I'm bootstrapping this and funding out of my own pocket. Thank you for your understanding!

Target Market(s)

Young adults who are just starting their careers, late teens and early 20s.

Font styles to use
Sans Serif

Requirements
Must have
• Ease of use, smart and sleek, a guided setup wizard which will help users setup their account after signing up.
Should not have
• Clunky

```html
<!DOCTYPE html>
<html lang="en">
<head>
<meta charset="utf-8">
<title>Expense Tracker – Welcome and Sign Up</title>
<link href="https://fonts.googleapis.com/css2?family=Poppins:wght@300;400;500&display=swap" rel="stylesheet">
<style>
  :root {
    --canvas-bg: #c9d1dc;
    --screen-white: #ffffff;
    --screen-soft: #f7f7f8;
    --field-bg: #f2f2f4;
    --brand-red: #d4112f;
    --brand-red-dark: #b80f2a;
    --brand-red-light: #ec1a3a;
    --social-blue: #3a5896;
    --text-dark: #222428;
    --text-muted: #7a7d84;
    --text-faint: #c2c4c9;
  }
  * { box-sizing: border-box; margin: 0; padding: 0; }
  html, body { width: 1200px; height: 985px; overflow: hidden; }
  body {
    background: var(--canvas-bg);
    font-family: "Poppins", sans-serif;
    position: relative;
  }
  .screen {
    position: absolute;
    top: 115px;
    width: 320px;
    height: 700px;
    border-radius: 34px;
    overflow: hidden;
    background: var(--screen-white);
    box-shadow: 0 18px 40px rgba(90, 100, 120, 0.18);
  }
  .screen--welcome { left: 149px; }
  .screen--signup { left: 705px; background: var(--screen-soft); }

  .status-bar {
    position: absolute; top: 0; left: 0; right: 0; height: 70px;
    z-index: 3;
  }
  .status-bar__time {
    position: absolute; top: 35px; left: 0; right: 0;
    text-align: center; font-size: 15px; font-weight: 400; color: var(--text-dark);
  }
  .status-bar__wifi { position: absolute; top: 40px; left: 24px; }
  .status-bar__signal { position: absolute; top: 40px; right: 22px; }
  .screen--signup .status-bar__time { color: #fff; }

  .app-badge {
    position: absolute; width: 110px; height: 110px; border-radius: 50%;
    background: #fff;
    display: flex; align-items: center; justify-content: center;
  }
  .app-badge__mark {
    font-size: 30px; font-weight: 500; color: var(--brand-red); letter-spacing: 1px;
  }
  .screen--welcome .app-badge {
    left: 107px; top: 207px;
    box-shadow: 0 0 28px rgba(0, 0, 0, 0.05);
  }

  .welcome__title {
    position: absolute; top: 330px; left: 0; right: 0; text-align: center;
    font-size: 27px; font-weight: 400; color: var(--brand-red);
  }
  .welcome__tagline {
    position: absolute; top: 368px; left: 0; right: 0; text-align: center;
    font-size: 9px; font-weight: 300; color: var(--text-muted);
  }

  .btn {
    position: absolute; left: 69px; width: 193px; height: 43px;
    border-radius: 22px; display: flex; align-items: center; justify-content: center;
    font-size: 13px; font-weight: 500;
  }
  .btn--primary {
    color: #fff;
    background: linear-gradient(90deg, var(--brand-red-dark), var(--brand-red-light));
    box-shadow: 0 8px 16px rgba(212, 17, 47, 0.25);
  }
  .btn--outline {
    color: var(--brand-red); font-weight: 400;
    border: 1.5px solid var(--brand-red); background: #fff;
  }
  .btn--social { background: var(--social-blue); color: #fff; }
  .screen--welcome .btn--primary { top: 443px; }
  .screen--welcome .btn--outline { top: 499px; }

  .signup__header {
    position: absolute; top: 0; left: 0; right: 0; height: 312px;
    background: linear-gradient(90deg, var(--brand-red-dark), var(--brand-red-light));
  }
  .screen--signup .app-badge { left: 108px; top: 96px; }
  .signup__title {
    position: absolute; top: 220px; left: 0; right: 0; text-align: center;
    font-size: 27px; font-weight: 400; color: #fff;
  }
  .signup__card {
    position: absolute; left: 19px; top: 283px; width: 283px; height: 343px;
    background: #fff; border-radius: 8px;
  }
  .field {
    position: absolute; left: 36px; width: 213px; height: 40px;
    background: var(--field-bg); border-radius: 20px;
  }
  .field__icon { position: absolute; left: 13px; top: 9px; }
  .field__label {
    position: absolute; left: 42px; top: 7px;
    font-size: 8px; font-weight: 300; color: var(--text-faint);
  }
  .field__value {
    position: absolute; left: 42px; top: 17px;
    font-size: 11px; font-weight: 400; color: var(--text-dark);
  }
  .field--name { top: 37px; }
  .field--email { top: 90px; }
  .field--password { top: 143px; }
  .signup__card .btn { left: 50px; }
  .signup__card .btn--primary { top: 216px; }
  .signup__card .btn--social { top: 273px; }
  .signup__footer {
    position: absolute; top: 657px; left: 0; right: 0; text-align: center;
    font-size: 9px; font-weight: 300; color: var(--text-muted);
  }
  .signup__footer-link { font-weight: 500; color: var(--text-dark); }
</style>
</head>
<body>

<section class="screen screen--welcome">
  <div class="status-bar">
    <svg class="status-bar__wifi" width="14" height="12" viewBox="0 0 14 12" fill="none" stroke="#222428" stroke-width="1.4" stroke-linecap="round">
      <path d="M1 4a9 9 0 0 1 12 0"/><path d="M3 6.5a6 6 0 0 1 8 0"/><path d="M5 9a3 3 0 0 1 4 0"/>
    </svg>
    <div class="status-bar__time">22:14</div>
    <svg class="status-bar__signal" width="30" height="12" viewBox="0 0 30 12">
      <rect x="0" y="9" width="2" height="3" fill="#222428"/><rect x="4" y="6" width="2" height="6" fill="#222428"/>
      <rect x="8" y="3" width="2" height="9" fill="#222428"/><rect x="12" y="0" width="2" height="12" fill="#c2c4c9"/>
      <rect x="22" y="1" width="7" height="11" rx="1" fill="#222428"/>
    </svg>
  </div>

  <div class="app-badge"><span class="app-badge__mark">ET</span></div>
  <h1 class="welcome__title">Expense Tracker</h1>
  <p class="welcome__tagline">Expense Tracker App for Young Adults</p>

  <div class="btn btn--primary">Sign Up</div>
  <div class="btn btn--outline">Sign In</div>
</section>

<section class="screen screen--signup">
  <div class="signup__header"></div>
  <div class="status-bar">
    <svg class="status-bar__wifi" width="14" height="12" viewBox="0 0 14 12" fill="none" stroke="#ffffff" stroke-width="1.4" stroke-linecap="round">
      <path d="M1 4a9 9 0 0 1 12 0"/><path d="M3 6.5a6 6 0 0 1 8 0"/><path d="M5 9a3 3 0 0 1 4 0"/>
    </svg>
    <div class="status-bar__time">22:14</div>
    <svg class="status-bar__signal" width="30" height="12" viewBox="0 0 30 12">
      <rect x="0" y="9" width="2" height="3" fill="#fff"/><rect x="4" y="6" width="2" height="6" fill="#fff"/>
      <rect x="8" y="3" width="2" height="9" fill="#fff"/><rect x="12" y="0" width="2" height="12" fill="#f5a3b0"/>
      <rect x="22" y="1" width="7" height="11" rx="1" fill="#fff"/>
    </svg>
  </div>

  <div class="app-badge"><span class="app-badge__mark">ET</span></div>
  <h1 class="signup__title">Sign Up</h1>

  <form class="signup__card">
    <div class="field field--name">
      <svg class="field__icon" width="18" height="22" viewBox="0 0 18 22" fill="none" stroke="#b4b6bc" stroke-width="1.1">
        <circle cx="9" cy="6" r="4.5"/><path d="M1 20c0-4.5 3.5-7 8-7s8 2.5 8 7z"/>
      </svg>
      <span class="field__label">Full Name</span>
      <span class="field__value">Leo Marsh</span>
    </div>
    <div class="field field--email">
      <svg class="field__icon" width="20" height="22" viewBox="0 0 20 22" fill="none" stroke="#b4b6bc" stroke-width="1.1">
        <rect x="1" y="5" width="18" height="12"/><path d="M1 5l9 7 9-7M1 17l7-6M19 17l-7-6"/>
      </svg>
      <span class="field__label">Email</span>
      <span class="field__value">leo.marsh@mailnest.com</span>
    </div>
    <div class="field field--password">
      <svg class="field__icon" width="18" height="22" viewBox="0 0 18 22" fill="none" stroke="#b4b6bc" stroke-width="1.1">
        <path d="M4 10V6a5 5 0 0 1 10 0v4"/><rect x="1.5" y="10" width="15" height="11" rx="1.5"/><circle cx="9" cy="15.5" r="1.4"/>
      </svg>
      <span class="field__label">Password</span>
      <span class="field__value">**************</span>
    </div>

    <div class="btn btn--primary">Sign Up</div>
    <div class="btn btn--social">Circlenet</div>
  </form>

  <p class="signup__footer">Already have an account? <span class="signup__footer-link">Sign In</span></p>
</section>

</body>
</html>
```